Podcast cover art for Steady Harbor Podcast for Busy Parents

I am relaunching my 3 year podcast under a new name. The podcast is called Steady Harbor for Busy Parents. The parent company is called Bright Path Studio (see attached logo) and should be represented on the cover in a small way. Previously the show was called Bright Path Studio. We talk about creating life balance for working moms by focusing on faith, marriage, parenting, career, health, home, finances, and friends/fun. I don't mind having stock photography on the cover but I prefer not to have my image on it as it is not a personal brand. I have attached a couple of stock images as inspiration.

Target Market(s)

working Christian moms age 30-45 income 75,000+, working full time, Christian faith, married

Industry/Entity Type

Media

Font styles to use
Serif

Requirements
Must have
• Podcast name: Steady Harbor for Busy Parents
• By: Bright Path Studio (include logo)
• I also included my brand sheet for reference which includes my brand colors and fonts. Navy should be the primary with orange and gray as the accents
Should not have
• No flowers, or overly girly. My brand is more clean, preppy, and young-sophisticated.

```html
<!DOCTYPE html>
<html lang="en">
<head>
<meta charset="UTF-8">
<title>Steady Harbor for Busy Parents — Cover Art</title>
<link rel="stylesheet" href="https://fonts.googleapis.com/css2?family=Libre+Baskerville:ital@1&family=Montserrat:wght@400;700&display=swap">
<style>
  :root {
    --navy: #1b2a4e;
    --navy-deep: #131f3b;
    --orange-deep: #e0772f;
    --orange-mid: #ee8a3c;
    --orange-soft: #f2a052;
    --glow: #ffd66e;
    --gray: #c9ccd2;
    --white: #ffffff;
  }
  * { margin: 0; padding: 0; box-sizing: border-box; }
  html, body {
    width: 1200px;
    height: 1200px;
    overflow: hidden;
    background: var(--navy);
  }
  .cover {
    position: relative;
    width: 1200px;
    height: 1200px;
    overflow: hidden;
  }
  .cover-photo {
    position: absolute;
    inset: 0;
    background:
      radial-gradient(circle at 50% 22%, var(--glow) 0%, rgba(255, 200, 100, 0.6) 14%, rgba(242, 160, 82, 0) 44%),
      linear-gradient(180deg, var(--orange-soft) 0%, var(--orange-mid) 45%, var(--orange-deep) 100%);
  }
  .cover-frame {
    position: absolute;
    inset: 0;
    border: 24px solid var(--navy);
    pointer-events: none;
  }
  .title { position: absolute; inset: 0; }
  .title-line {
    position: absolute;
    left: 0;
    right: 0;
    text-align: center;
    line-height: 1;
    white-space: nowrap;
  }
  .title-script {
    font-family: "Libre Baskerville", Georgia, serif;
    font-style: italic;
    font-weight: 400;
    color: var(--navy);
  }
  .title-script--lead { top: 121px; font-size: 140px; }
  .title-script--join { top: 505px; font-size: 100px; }
  .title-bold {
    font-family: "Montserrat", Arial, sans-serif;
    font-weight: 700;
    color: var(--white);
    text-transform: uppercase;
    font-size: 185px;
    letter-spacing: 1px;
  }
  .title-bold--harbor { top: 291px; }
  .title-bold--busy { top: 631px; }
  .title-bold--parents { top: 791px; }
  .studio-mark {
    position: absolute;
    left: 0;
    right: 0;
    top: 1100px;
    display: flex;
    align-items: center;
    justify-content: center;
    gap: 14px;
  }
  .studio-dot {
    width: 18px;
    height: 18px;
    border-radius: 50%;
    background: var(--navy);
  }
  .studio-name {
    font-family: "Montserrat", Arial, sans-serif;
    font-weight: 400;
    font-size: 44px;
    line-height: 1;
    color: var(--navy-deep);
  }
</style>
</head>
<body>
  <main class="cover">
    <div class="cover-photo" role="img" aria-label="Stock photo: a woman standing by a lake at sunset with her arms stretched wide, bathed in warm orange light"></div>
    <div class="cover-frame"></div>
    <h1 class="title">
      <span class="title-line title-script title-script--lead">Steady</span>
      <span class="title-line title-bold title-bold--harbor">Harbor</span>
      <span class="title-line title-script title-script--join">for</span>
      <span class="title-line title-bold title-bold--busy">Busy</span>
      <span class="title-line title-bold title-bold--parents">Parents</span>
    </h1>
    <div class="studio-mark">
      <span class="studio-dot"></span>
      <span class="studio-name">Bright Path Studio</span>
    </div>
  </main>
</body>
</html>
```